Business Card Design

Im electrician in melbourne after a business cards. I have no logos done. I have attached a card that i like but needs to be altered to my business name, so in the picture shows a lead plug into a socket spelling plug, i want the spelling replaced with my company name. I was thinking some thing with a charcoal back ground with yellow or green font.
I have wrote what I'd like above but feel free to try your own ideas and designs.
Industry/Entity Type
Electrician
Contact Information for Business Card
Zint Electrical Services PTY LTD (Display on the front of card, the PTY LTD can be in small font)
REC:58194 (also on the front in small font)
Call Teodor (back i dont want my last name on the card)
Phone: 0488571039 (back
Email: zintelectricalservices@mailnest.example (back)
Domestic, Commercial, Industrial, (on the back in dot points.)
Look and feel
Each slider illustrates characteristics of the customer's brand and the style your logo design should communicate.

```html
<!DOCTYPE html>
<html lang="en">
<head>
<meta charset="utf-8">
<title>Zint Electrical Services – Business Card</title>
<link rel="stylesheet" href="https://fonts.googleapis.com/css2?family=Ubuntu:wght@300;400&family=Exo+2:wght@300&display=swap">
<style>
  :root {
    --paper: #ffffff;
    --charcoal: #454141;
    --volt-green: #8fd14f;
  }
  * { box-sizing: border-box; margin: 0; padding: 0; }
  html, body {
    width: 952px;
    height: 1200px;
    overflow: hidden;
    background: var(--paper);
  }
  .sheet {
    position: relative;
    width: 952px;
    height: 1200px;
  }
  .card {
    position: absolute;
    left: 0;
    width: 952px;
    height: 574px;
    background: var(--charcoal);
    color: var(--volt-green);
    font-family: "Ubuntu", sans-serif;
  }
  .card--front { top: 0; }
  .card--back { top: 626px; }

  .brand-square {
    position: absolute;
    background: var(--volt-green);
    border-radius: 6px;
  }

  /* Front */
  .front-square { left: 69px; top: 184px; width: 42px; height: 42px; }
  .company-name {
    position: absolute;
    left: 128px;
    top: 176px;
    font-weight: 300;
    font-size: 52px;
    line-height: 60px;
    white-space: nowrap;
  }
  .company-reg {
    position: absolute;
    left: 578px;
    top: 276px;
    font-weight: 300;
    font-size: 18px;
    letter-spacing: 0.02em;
    white-space: nowrap;
  }
  .company-reg .reg-number { margin-left: 14px; }
  .service-list {
    position: absolute;
    left: 0;
    top: 428px;
    width: 952px;
    text-align: center;
    font-family: "Exo 2", sans-serif;
    font-weight: 300;
    font-size: 31px;
    letter-spacing: 0.2em;
    list-style: none;
    white-space: nowrap;
  }
  .service-list li { display: inline; }
  .service-list .divider { margin: 0 0.5em; }

  /* Back */
  .call-label {
    position: absolute;
    left: 282px;
    top: 100px;
    font-weight: 300;
    font-size: 38px;
  }
  .back-square { left: 282px; top: 155px; width: 66px; height: 64px; border-radius: 9px; }
  .contact-name {
    position: absolute;
    left: 368px;
    top: 142px;
    font-weight: 300;
    font-size: 76px;
    line-height: 90px;
  }
  .contact-details {
    position: absolute;
    left: 0;
    top: 352px;
    width: 952px;
    text-align: center;
    font-weight: 300;
    font-size: 33px;
    line-height: 57px;
  }
</style>
</head>
<body>
<main class="sheet">
  <section class="card card--front" aria-label="Card front">
    <span class="brand-square front-square"></span>
    <h1 class="company-name">Zint Electrical Services</h1>
    <p class="company-reg">PTY LTD<span class="reg-number">REC:58194</span></p>
    <ul class="service-list">
      <li>Domestic</li><li class="divider">|</li><li>Commercial</li><li class="divider">|</li><li>Industrial</li>
    </ul>
  </section>

  <section class="card card--back" aria-label="Card back">
    <p class="call-label">Call</p>
    <span class="brand-square back-square"></span>
    <h2 class="contact-name">Teodor</h2>
    <div class="contact-details">
      <p class="contact-phone">Phone: 0488571039</p>
      <p class="contact-email">Email: zintelectricalservices@mailnest.example</p>
    </div>
  </section>
</main>
</body>
</html>
```